IT Professional business card with a hometown feel and a little edgy.

My business name is Tamble Website Solutions. But I have ended up doing much more. I live in a very small remote community, where everyone knows everyone. We like the one-on-one customer service in this community. I do computer tutoring, virus removal, networking, and software training. My clients are businesses and private individuals.

My website is tamblewebsitesolutions.example, when I first designed it I was going for a fresh, clean look, which I still like. But I am thinking about making the website a bit more edgy to match my new logo from ArtHively (logo attached). At this time my website does not display the new logo, but I plan on redesigning the website in the future to match the logo and business card.

My tag line is "your local help for all things online"

I'm thinking I would like to have the business card printed with a metallic finish.
Updates

Please do not use black backgrounds, or any solid dark colors. Prefer light or white backgrounds.

Target Market(s)

Small businesses. Individuals that need computer help at home.

Industry/Entity Type

It Company

Contact Information for Business Card

Nora Prandell
Tamble Website Solutions
PO Box 7153
Calder, WA 98412
Cell: 555-271-3096
nora@tamblewebsitesolutions.example
tamblewebsitesolutions.example

Font styles to use
Serif

Requirements
Must have
• Must have all the information listed in "Business Card Details"
• Must use the logo provided.
• Use the colors from the provided logo
Nice to have
• Would like to use my tagline "your local help for all things online" all lowercase

```html
<!DOCTYPE html>
<html lang="en">
<head>
<meta charset="utf-8">
<title>Tamble Website Solutions – Business Card</title>
<link href="https://fonts.googleapis.com/css2?family=Open+Sans:wght@400;600;700&display=swap" rel="stylesheet">
<style>
  :root {
    --page-bg: #eeeeee;
    --card-white: #ffffff;
    --ink: #2b2b2b;
    --brand-green: #3f8a2f;
    --rule: #8a8a8a;
    --silver-light: #e4e4e4;
    --silver-mid: #c9c9c9;
    --silver-dark: #a9a9a9;
    --silver-ink: #8d8d8d;
    --tagline-ink: #6f6f6f;
  }
  * { box-sizing: border-box; margin: 0; padding: 0; }
  html, body { width: 1200px; height: 789px; overflow: hidden; }
  body {
    background: var(--page-bg);
    font-family: "Open Sans", sans-serif;
    position: relative;
  }
  .card {
    position: absolute;
    top: 240px;
    width: 540px;
    height: 310px;
    border-radius: 3px;
    box-shadow: 0 6px 18px rgba(0,0,0,0.12);
    overflow: hidden;
  }

  /* Front: contact side */
  .card-front { left: 45px; background: var(--card-white); }
  .front-brand {
    position: absolute; left: 40px; top: 30px;
    display: flex; align-items: center; gap: 14px;
  }
  .brand-square {
    width: 46px; height: 46px;
    background: var(--brand-green);
  }
  .brand-name {
    font-size: 17px; font-weight: 600; line-height: 1.15;
    color: var(--brand-green);
    padding-left: 14px;
    border-left: 1px solid var(--rule);
  }
  .front-rule-h {
    position: absolute; left: 40px; right: 40px; top: 120px;
    height: 1px; background: var(--rule);
  }
  .front-rule-v {
    position: absolute; left: 230px; top: 120px;
    width: 1px; height: 160px; background: var(--rule);
  }
  .contact {
    position: absolute; left: 252px; top: 132px;
    color: var(--ink); font-size: 11.5px; line-height: 1.5;
  }
  .contact-name { font-size: 17px; font-weight: 700; margin-bottom: 4px; }
  .contact-block + .contact-block { margin-top: 8px; }
  .contact-company { color: var(--brand-green); font-weight: 600; }

  /* Back: metallic side */
  .card-back {
    left: 615px;
    background: linear-gradient(135deg, var(--silver-light) 0%, var(--silver-mid) 55%, var(--silver-dark) 100%);
  }
  .back-brand {
    position: absolute; left: 0; right: 0; top: 92px;
    display: flex; justify-content: center; align-items: center; gap: 16px;
  }
  .back-brand .brand-square { background: var(--silver-ink); opacity: 0.55; width: 52px; height: 52px; }
  .back-brand .brand-name {
    color: var(--silver-ink); font-size: 19px; font-weight: 600;
    border-left-color: var(--silver-ink);
  }
  .tagline {
    position: absolute; left: 0; right: 0; top: 210px;
    text-align: center;
    font-size: 13px; font-weight: 600; letter-spacing: 3px;
    color: var(--tagline-ink);
  }
</style>
</head>
<body>
  <section class="card card-front" aria-label="Business card front">
    <div class="front-brand">
      <span class="brand-square"></span>
      <span class="brand-name">Tamble<br>Website<br>Solutions</span>
    </div>
    <div class="front-rule-h"></div>
    <div class="front-rule-v"></div>
    <div class="contact">
      <div class="contact-name">Nora Prandell</div>
      <div class="contact-block">
        Cell: 555-271-3096<br>
        nora@tamblewebsitesolutions.example<br>
        tamblewebsitesolutions.example
      </div>
      <div class="contact-block">
        <span class="contact-company">Tamble Website Solutions</span><br>
        PO Box 7153<br>
        Calder, WA 98412
      </div>
    </div>
  </section>

  <section class="card card-back" aria-label="Business card back">
    <div class="back-brand">
      <span class="brand-square"></span>
      <span class="brand-name">Tamble<br>Website<br>Solutions</span>
    </div>
    <p class="tagline">your local help for all things online</p>
  </section>
</body>
</html>
```